brightpath Business Card

Already have the logo, but now need the business card design

Industry/Entity Type

Business Software

Contact Information for Business Card

web site will be brightpath.io / The card should have the person name / position / mobile / email / and company address

Colors

Designer to choose colors to be used in the design.

Requirements
Must have
• See business card details
• One side to have the brightpath logo
Nice to have
• If possible the 'O' from flow can be watermarked into the second side
• Try to fit in the words brightpath Business Solutions

```html
<!DOCTYPE html>
<html lang="en">
<head>
<meta charset="utf-8">
<title>brightpath Business Card</title>
<link href="https://fonts.googleapis.com/css2?family=Roboto:wght@400;500&display=swap" rel="stylesheet">
<style>
  :root {
    --page-bg: #eef0f0;
    --card-dark: #141417;
    --card-light: #ffffff;
    --brand-grey: #6d6e71;
    --text-grey-dark: #8a8b8e;
    --text-grey-light: #6d6e71;
    --accent-red: #e3202a;
    --divider: #7a7b7e;
  }
  * { box-sizing: border-box; margin: 0; padding: 0; }
  html, body {
    width: 1200px; height: 900px; overflow: hidden;
    background: var(--page-bg);
    font-family: "Roboto", Arial, sans-serif;
  }
  .sheet { position: relative; width: 1200px; height: 900px; }

  .card {
    position: absolute;
    width: 514px; height: 296px;
    box-shadow: 0 1px 4px rgba(0,0,0,0.18);
    overflow: hidden;
  }
  .card--dark { background: var(--card-dark); }
  .card--light { background: var(--card-light); }
  .card--front-dark { left: 73px; top: 138px; }
  .card--back-dark { left: 614px; top: 138px; }
  .card--front-light { left: 73px; top: 463px; }
  .card--back-light { left: 614px; top: 463px; }

  .wordmark {
    position: absolute; left: 0; right: 0; top: 108px;
    text-align: center;
  }
  .wordmark__name {
    display: block;
    font-size: 58px; font-weight: 400; line-height: 1;
    letter-spacing: -1px;
    color: var(--brand-grey);
  }
  .wordmark__tagline {
    display: block; margin-top: 6px;
    font-size: 10.5px; font-weight: 400;
    letter-spacing: 6.2px; text-transform: uppercase;
    color: var(--brand-grey);
  }

  .person {
    position: absolute; right: 277px; top: 131px;
    text-align: right;
  }
  .person__name {
    font-size: 16px; font-weight: 500; line-height: 1.1;
    text-transform: uppercase;
  }
  .card--dark .person__name { color: var(--text-grey-dark); }
  .card--light .person__name { color: var(--text-grey-light); }
  .person__role {
    font-size: 11.5px; font-weight: 500; margin-top: 2px;
    text-transform: uppercase; color: var(--accent-red);
  }
  .divider {
    position: absolute; left: 258px; top: 104px;
    width: 1px; height: 87px; background: var(--divider);
  }
  .contacts {
    position: absolute; left: 277px; top: 113px;
    list-style: none;
  }
  .contacts__item {
    display: flex; align-items: center; gap: 6px;
    height: 18px;
    font-size: 14px;
  }
  .card--dark .contacts__item { color: var(--text-grey-dark); }
  .card--light .contacts__item { color: var(--text-grey-light); }
  .contacts__icon { width: 11px; height: 11px; fill: var(--accent-red); flex: none; }
  .card .contacts__item--web { color: var(--accent-red); padding-left: 2px; }
  .address {
    position: absolute; left: 0; width: 516px; top: 254px;
    text-align: center; font-size: 14px;
  }
  .card--dark .address { color: var(--text-grey-dark); }
  .card--light .address { color: var(--text-grey-light); }
</style>
</head>
<body>
<main class="sheet">

  <section class="card card--dark card--front-dark">
    <div class="wordmark">
      <span class="wordmark__name">brightpath</span>
      <span class="wordmark__tagline">Business Solutions</span>
    </div>
  </section>

  <section class="card card--dark card--back-dark">
    <div class="person">
      <p class="person__name">Daniel Marlowe</p>
      <p class="person__role">Managing Director</p>
    </div>
    <div class="divider"></div>
    <ul class="contacts">
      <li class="contacts__item"><svg class="contacts__icon" viewBox="0 0 12 12"><path d="M1 4.5C1 3 3 2 6 2s5 1 5 2.5L9 5.5 8 4H4L3 5.5z"/><rect x="3" y="6" width="6" height="4" rx="1"/></svg>555 014 26 83</li>
      <li class="contacts__item"><svg class="contacts__icon" viewBox="0 0 12 12"><path d="M3.5 0.5h5v11h-5z M4.5 1.5v8h3v-8z" fill-rule="evenodd"/></svg>555 019 37 42</li>
      <li class="contacts__item"><svg class="contacts__icon" viewBox="0 0 12 12"><path d="M0.5 2.5h11L6 6.5z M0.5 3.8L6 7.8l5.5-4V10h-11z"/></svg>d.marlowe@brightpath.io</li>
      <li class="contacts__item contacts__item--web">www.brightpath.io</li>
    </ul>
    <p class="address">48 Harbor Lane, Millbrook, New York 12545</p>
  </section>

  <section class="card card--light card--front-light">
    <div class="wordmark">
      <span class="wordmark__name">brightpath</span>
      <span class="wordmark__tagline">Business Solutions</span>
    </div>
  </section>

  <section class="card card--light card--back-light">
    <div class="person">
      <p class="person__name">Daniel Marlowe</p>
      <p class="person__role">Managing Director</p>
    </div>
    <div class="divider"></div>
    <ul class="contacts">
      <li class="contacts__item"><svg class="contacts__icon" viewBox="0 0 12 12"><path d="M1 4.5C1 3 3 2 6 2s5 1 5 2.5L9 5.5 8 4H4L3 5.5z"/><rect x="3" y="6" width="6" height="4" rx="1"/></svg>555 014 26 83</li>
      <li class="contacts__item"><svg class="contacts__icon" viewBox="0 0 12 12"><path d="M3.5 0.5h5v11h-5z M4.5 1.5v8h3v-8z" fill-rule="evenodd"/></svg>555 019 37 42</li>
      <li class="contacts__item"><svg class="contacts__icon" viewBox="0 0 12 12"><path d="M0.5 2.5h11L6 6.5z M0.5 3.8L6 7.8l5.5-4V10h-11z"/></svg>d.marlowe@brightpath.io</li>
      <li class="contacts__item contacts__item--web">www.brightpath.io</li>
    </ul>
    <p class="address">48 Harbor Lane, Millbrook, New York 12545</p>
  </section>

</main>
</body>
</html>
```